Palu Sales Pipeline

We need an infographic to help the sales team understand the importance of a sales pipeline and how to grow and manage it. It's important that they understand every process plays a vital part and a complete circle. If you break one part, the sales process can be a failure.

Font styles to use
Serif

Colors
33b8a4
abd037

Requirements
Must have
• Have fun!
Nice to have
• Open to all ideas. Keep in mind that we are eastern philosophy focused!
Should not have
• Not applicable! Just have phone

```html
<!DOCTYPE html>
<html lang="en">
<head>
<meta charset="utf-8">
<title>Palu Sales Pipeline Lifecycle</title>
<link rel="stylesheet" href="https://fonts.googleapis.com/css2?family=Lato:wght@400;700;900&family=Gochi+Hand&display=swap">
<style>
  :root {
    --navy: #0d3573;
    --teal: #33b8a4;
    --teal-deep: #2a9a88;
    --green: #abd037;
    --green-bright: #b9da3c;
    --green-light: #c6e443;
    --white: #ffffff;
    --backdrop: #e9ecee;
  }
  * { margin: 0; padding: 0; box-sizing: border-box; }
  html, body {
    width: 1200px; height: 1200px; overflow: hidden;
    background: var(--backdrop);
  }
  .poster {
    position: absolute; left: 141px; top: 6px;
    width: 764px; height: 990px;
    background: var(--white);
    transform: scale(1.2); transform-origin: 0 0;
    overflow: hidden;
    font-family: "Lato", sans-serif;
  }
  .header-band {
    position: absolute; left: 200px; top: 0; right: 0; height: 108px;
    background: var(--navy);
  }
  .poster-title {
    position: absolute; left: 272px; top: 34px;
    color: var(--white); font-size: 35px; font-weight: 400; letter-spacing: 0.5px;
    white-space: nowrap;
  }
  .brand-plate {
    position: absolute; left: -60px; top: -140px;
    width: 320px; height: 290px; border-radius: 50%;
    background: var(--white);
    box-shadow: 0 6px 14px rgba(0,0,0,0.18);
  }
  .brand-name {
    position: absolute; left: 36px; top: 30px;
    display: flex; align-items: center; gap: 10px;
    color: var(--navy); font-size: 50px; font-weight: 900;
  }
  .brand-dot {
    width: 40px; height: 40px; border-radius: 50%; background: var(--teal);
  }
  .lifecycle { position: absolute; left: 0; top: 0; width: 764px; height: 990px; }
  .stage-label { font-family: "Lato", sans-serif; font-weight: 700; font-size: 14px; fill: var(--white); }
  .hand { font-family: "Gochi Hand", cursive; }
  .footer-band {
    position: absolute; left: 0; right: 0; bottom: 0; height: 57px;
    background: var(--teal);
    display: flex; align-items: center; justify-content: center; gap: 12px;
    color: var(--white); font-size: 22px; font-weight: 700;
  }
</style>
</head>
<body>
  <main class="poster">
    <div class="header-band"></div>
    <h1 class="poster-title">SALES PIPELINE LIFECYCLE</h1>
    <div class="brand-plate"></div>
    <div class="brand-name"><span class="brand-dot"></span><span>Palu</span></div>

    <svg class="lifecycle" viewBox="0 0 764 990" xmlns="http://www.w3.org/2000/svg">
      <defs>
        <linearGradient id="orbit-stroke" x1="0" y1="0" x2="1" y2="0">
          <stop offset="0" stop-color="#33b8a4"/>
          <stop offset="1" stop-color="#abd037"/>
        </linearGradient>
      </defs>

      <circle class="outer-orbit" cx="375" cy="543" r="280" fill="none" stroke="url(#orbit-stroke)" stroke-width="4"/>

      <g class="stage-ring" fill="none" stroke-width="96">
        <path d="M307.4,712.2 A180,180 0 0 1 199.9,481.4" stroke="#2a9a88"/>
        <path d="M199.9,481.4 A180,180 0 0 1 265.7,395.6" stroke="#33b8a4"/>
        <path d="M265.7,395.6 A180,180 0 0 1 496.3,415.7" stroke="#abd037"/>
        <path d="M496.3,415.7 A180,180 0 0 1 538.1,604.6" stroke="#b9da3c"/>
        <path d="M538.1,604.6 A180,180 0 0 1 353.3,722.3" stroke="#c6e443"/>
      </g>

      <text class="stage-label" x="369" y="371" text-anchor="middle">ENGAGEMENT</text>
      <text class="stage-label" x="559" y="497" text-anchor="middle">PEAK/</text>
      <text class="stage-label" x="559" y="513" text-anchor="middle">SUMMIT</text>
      <text class="stage-label" x="464" y="696" text-anchor="middle">RETENTION</text>
      <text class="stage-label" x="464" y="712" text-anchor="middle">/DESCENT</text>
      <text class="stage-label" x="248" y="699" text-anchor="middle">COLLECTION</text>
      <text class="stage-label" x="248" y="715" text-anchor="middle">/BUILD UP</text>
      <text class="stage-label" x="187" y="498" text-anchor="middle">NURTURE</text>
      <text class="stage-label" x="187" y="514" text-anchor="middle">/RAPPORT</text>

      <text class="hand" x="369" y="530" text-anchor="middle" font-size="120" fill="#33b8a4">5</text>
      <text class="hand" x="379" y="578" text-anchor="middle" font-size="46" fill="#0d3573">Key</text>
      <text class="hand" x="379" y="630" text-anchor="middle" font-size="48" fill="#0d3573">Focuses</text>

      <g class="stage-icon">
        <circle cx="382" cy="263" r="32" fill="#fff" stroke="#abd037" stroke-width="3"/>
        <circle cx="382" cy="263" r="26" fill="#abd037" role="img" aria-label="Pruning shears icon"/>
      </g>
      <g class="stage-icon">
        <circle cx="647" cy="498" r="32" fill="#fff" stroke="#b9da3c" stroke-width="3"/>
        <circle cx="647" cy="498" r="26" fill="#b9da3c" role="img" aria-label="Packaged plant icon"/>
      </g>
      <g class="stage-icon">
        <circle cx="597" cy="713" r="32" fill="#fff" stroke="#c6e443" stroke-width="3"/>
        <circle cx="597" cy="713" r="26" fill="#c6e443" role="img" aria-label="Grown plant icon"/>
      </g>
      <g class="stage-icon">
        <circle cx="91" cy="493" r="32" fill="#fff" stroke="#33b8a4" stroke-width="3"/>
        <circle cx="91" cy="493" r="26" fill="#33b8a4" role="img" aria-label="Water and sun icon"/>
      </g>
      <g class="stage-icon">
        <circle cx="146" cy="715" r="32" fill="#fff" stroke="#2a9a88" stroke-width="3"/>
        <circle cx="146" cy="715" r="26" fill="#2a9a88" role="img" aria-label="Planting seeds icon"/>
      </g>

      <text class="hand" x="388" y="224" text-anchor="middle" font-size="19" fill="#abd037">Harvest/Prune</text>
      <text class="hand" x="72" y="434" text-anchor="middle" font-size="19" fill="#33b8a4">Water</text>
      <text class="hand" x="80" y="450" text-anchor="middle" font-size="19" fill="#33b8a4">/Sun</text>
      <text class="hand" x="694" y="440" text-anchor="middle" font-size="19" fill="#abd037">Package/</text>
      <text class="hand" x="696" y="457" text-anchor="middle" font-size="19" fill="#abd037">Presentation</text>
      <text class="hand" x="655" y="723" text-anchor="middle" font-size="19" fill="#abd037">Plant</text>
      <text class="hand" x="117" y="775" text-anchor="middle" font-size="19" fill="#2a9a88">Seed/Plant</text>
    </svg>

    <footer class="footer-band">
      <svg width="24" height="24" viewBox="0 0 24 24" fill="none" stroke="#fff" stroke-width="2" aria-hidden="true">
        <circle cx="12" cy="12" r="10"/>
        <ellipse cx="12" cy="12" rx="4.5" ry="10"/>
        <line x1="2" y1="12" x2="22" y2="12"/>
        <line x1="4" y1="7" x2="20" y2="7"/>
        <line x1="4" y1="17" x2="20" y2="17"/>
      </svg>
      <span>www.palusales.com</span>
    </footer>
  </main>
</body>
</html>
```